A Training Firm needs a Brochure - Clearpath Onboarding Skills Brochure

Brevaloom, a HR Consulting Firm focused on Training & Development is seeking a Brochure Design for one of its training programs - Clearpath Onboarding Skills Program.

The designs should be innovative,image led and interesting to read. We would like to see designs that incorporate the colours Blue and Green. Because this company is based in Africa, we would like the designers to use image of Black people instead of Caucasians.

Brevaloom is a member of Tandrel Group, a HR Consulting firm that offers services in the area of Learning, Talent Solutions, Outsourcing and Strategy Consulting

Target Market(s)

CEOs, HR Directors, Heads of Learning and Learning Managers of Large, Medium and Small Scale Organisations in Nigeria

Industry/Entity Type

Training

Other font styles liked:
• Corbel

Colors
3176b5
abd036

Requirements
Must have
• Brevaloom Logo, A link with the Parent Company Tandrel Group (We usually add that Brevaloom is a member of the Tandrel Group) The Group Logo and the Pantone Colours have been attached
Nice to have
• The entire Brochure should be graphically led. That is, lots of graphics - Infographics/Images/colours etc
Should not have
• No Caucasian images. We are an African based Firm and would like to have African images

```html
<!DOCTYPE html>
<html lang="en">
<head>
<meta charset="utf-8">
<title>Clearpath Onboarding Skills Brochure</title>
<link rel="stylesheet" href="https://fonts.googleapis.com/css2?family=Source+Sans+3:wght@300;400;600;700&display=swap">
<style>
  :root {
    --teal: #137f93;
    --lime: #b7cf7f;
    --ink: #55595c;
    --heading: #1a7d8f;
    --logo: #1f4f6e;
    --paper: #ffffff;
  }
  * { margin: 0; padding: 0; box-sizing: border-box; }
  html, body { width: 850px; height: 1200px; overflow: hidden; background: var(--paper); }
  body { font-family: "Source Sans 3", sans-serif; color: var(--ink); position: relative; }

  .title-band {
    position: absolute; left: 0; top: 60px; width: 788px; height: 121px;
    background: var(--teal); color: #fff; padding: 16px 0 0 60px;
  }
  .title-band h1 { font-size: 32px; font-weight: 700; line-height: 1.2; }
  .title-band .subtitle { font-size: 32px; font-weight: 300; line-height: 1.2; }
  .title-accent { position: absolute; left: 788px; top: 60px; width: 62px; height: 121px; background: var(--lime); }

  .hero-photo {
    position: absolute; left: 60px; top: 242px; width: 728px; height: 222px;
    background: linear-gradient(180deg, #9eb4c4 0%, #5f7f96 45%, #2f3e4c 78%, #4a3434 100%);
  }

  .content { position: absolute; left: 60px; top: 520px; width: 728px; }
  .content h2 { font-size: 21px; font-weight: 700; color: var(--heading); margin-bottom: 10px; }
  .content p { font-size: 15px; line-height: 19.4px; font-weight: 400; margin-bottom: 19px; }
  .content h2.spaced { margin-top: 14px; }

  .brand { position: absolute; left: 60px; top: 1146px; display: flex; align-items: center; gap: 10px; }
  .brand-name { font-size: 32px; font-weight: 600; color: var(--logo); line-height: 1; }
  .brand-mark { width: 22px; height: 22px; border-radius: 50%; background: var(--lime); }
  .brand-parent { position: absolute; left: 60px; top: 1181px; font-size: 9px; color: var(--logo); font-weight: 600; }

  .page-number {
    position: absolute; left: 788px; top: 1140px; width: 62px; height: 60px;
    background: var(--lime); color: #fff; font-size: 26px; font-weight: 400;
    display: flex; align-items: center; justify-content: center;
  }
</style>
</head>
<body>
  <header class="title-band">
    <h1>Clearpath Onboarding</h1>
    <div class="subtitle">Skills Program</div>
  </header>
  <div class="title-accent"></div>

  <div class="hero-photo" role="img" aria-label="City skyline of glass office towers at dusk with red light trails on the road"></div>

  <main class="content">
    <h2>Clearpath Onboarding Programmes</h2>
    <p>Engaging employees effectively and developing them early in their career in a new company is essential for high performance and business result. Survey results of a research on new employee induction conducted by Halvern Research reveals that the organisations that enjoy best-in-class performance shared several common characteristics, a key one being the quality, structure and effectiveness of their Induction Programme.</p>

    <h2 class="spaced">Why You Need Our Clearpath Onboarding Solution</h2>
    <p>In the light of significant decline in the quality of education and the preparedness of employees entering into the workplace, organisations that have a Talent Mindset must invest in “Growing Their Own Talent”. This investment requires a partner like Brevaloom that understands what it takes to successful induct new employees. Partnering with our firm on your induction needs will significantly increase your probability of success.</p>
    <p>Brevaloom's Clearpath Onboarding intervention is the Strategic process designed to effectively and proactively engage new employees (both experienced and fresh graduates), acclimate them into the organisation's culture and prepare them adequately to contribute to a desired level as quickly as possible, in other words, “hit the ground running”.</p>
    <p>With our experience and deep expertise in the area recruiting and helping to induct thousands of employees on a yearly basis over the past 10 years, we know what works and what doesn't as far as a company's objective for bringing a new employee on board is concerned. We can assist you in designing a best-in-class induction programme that will ensure your newly hired employees start to contribute meaningfully to your organisation as early as needful. We offer Turnkey Induction Programme Design and Implementation from quality candidate sourcing and on-boarding to enabling superior performance on the job.</p>
  </main>

  <footer>
    <div class="brand">
      <span class="brand-name">Brevaloom</span>
      <span class="brand-mark"></span>
    </div>
    <div class="brand-parent">by Tandrel Group</div>
    <div class="page-number">2</div>
  </footer>
</body>
</html>
```